Business Card Design

Freelance writer, coach, teacher and researcher specialising in improving mathematics teaching and learning in primary schools. I write books and articles for teachers, speak extensively at conferences in UK and aboard. Would like something with a cube in the design. Clean, modern - logo suitable for use on a website. Should NOT look 'childish' (no comic sans or chalkboard type fonts)

Full details to go on card:

Professor Dan Theroll
Unlocking Early Numeracy

info@dantheroll.net
#dantheroll26
www.dantheroll.net
+44 7812 660 394

Industry/Entity Type

Teacher

Contact Information for Business Card

Professor Dan Theroll
Unlocking Early Numbers

```html
<!DOCTYPE html>
<html lang="en">
<head>
<meta charset="utf-8">
<title>Professor Dan Theroll – Business Card</title>
<link rel="stylesheet" href="https://fonts.googleapis.com/css2?family=PT+Sans:wght@400&family=Zilla+Slab:wght@300&display=swap">
<style>
  :root {
    --page-bg: #f4f5f6;
    --card-light: #f7f8f9;
    --card-mid: #e6e9eb;
    --card-deep: #d6dadd;
    --cube-front: #eef0f1;
    --cube-top: #f8f9fa;
    --cube-side: #d3d7da;
    --cube-faint: #e1e4e6;
    --name-green: #4a7a2a;
    --tagline-blue: #3b82c4;
    --contact-grey: #4a4c4e;
  }
  * { margin: 0; padding: 0; box-sizing: border-box; }
  html, body {
    width: 998px;
    height: 1200px;
    overflow: hidden;
    background: var(--page-bg);
  }
  .canvas {
    position: relative;
    width: 998px;
    height: 1200px;
  }
  .business-card {
    position: absolute;
    left: 49px;
    top: 308px;
    width: 900px;
    height: 584px;
    overflow: hidden;
    box-shadow: 0 2px 10px rgba(0, 0, 0, 0.08);
  }
  .card-backdrop {
    position: absolute;
    inset: 0;
    width: 100%;
    height: 100%;
  }
  .cube-front { fill: var(--cube-front); }
  .cube-top { fill: var(--cube-top); }
  .cube-side { fill: var(--cube-side); }
  .cube-faint { fill: var(--cube-faint); }
  .card-content {
    position: absolute;
    inset: 0;
    text-align: center;
  }
  .brand-mark {
    position: absolute;
    left: 0;
    top: 122px;
    width: 900px;
    display: flex;
    flex-direction: column;
    align-items: center;
    gap: 10px;
  }
  .brand-square {
    width: 64px;
    height: 64px;
    background: var(--name-green);
  }
  .brand-name {
    font-family: "PT Sans", sans-serif;
    font-weight: 400;
    font-size: 17px;
    line-height: 1;
    color: var(--name-green);
  }
  .person-name {
    position: absolute;
    left: 0;
    top: 282px;
    width: 900px;
    font-family: "PT Sans", sans-serif;
    font-weight: 400;
    font-size: 46px;
    line-height: 1;
    color: var(--name-green);
  }
  .tagline {
    position: absolute;
    left: 0;
    top: 339px;
    width: 900px;
    font-family: "PT Sans", sans-serif;
    font-weight: 400;
    font-size: 25px;
    line-height: 1;
    color: var(--tagline-blue);
  }
  .contact-list {
    position: absolute;
    left: 0;
    top: 384px;
    width: 900px;
    list-style: none;
    font-family: "Zilla Slab", serif;
    font-weight: 300;
    font-size: 23px;
    line-height: 27.5px;
    color: var(--contact-grey);
  }
</style>
</head>
<body>
  <main class="canvas">
    <section class="business-card">
      <svg class="card-backdrop" viewBox="0 0 900 584" preserveAspectRatio="none" role="img" aria-label="Soft grey field of floating white cubes behind the card text">
        <defs>
          <radialGradient id="backdrop-glow" cx="50%" cy="40%" r="75%">
            <stop offset="0%" stop-color="var(--card-light)"/>
            <stop offset="65%" stop-color="var(--card-mid)"/>
            <stop offset="100%" stop-color="var(--card-deep)"/>
          </radialGradient>
        </defs>
        <rect width="900" height="584" fill="url(#backdrop-glow)"/>

        <g class="faint-cubes">
          <rect class="cube-faint" x="250" y="30" width="60" height="60"/>
          <rect class="cube-faint" x="370" y="10" width="40" height="40"/>
          <rect class="cube-faint" x="560" y="40" width="70" height="70"/>
          <rect class="cube-faint" x="660" y="20" width="50" height="50"/>
          <rect class="cube-faint" x="260" y="180" width="80" height="70"/>
          <rect class="cube-faint" x="580" y="190" width="55" height="55"/>
          <rect class="cube-faint" x="20" y="400" width="70" height="90"/>
          <rect class="cube-faint" x="330" y="500" width="90" height="70"/>
          <rect class="cube-faint" x="520" y="480" width="110" height="80"/>
          <rect class="cube-faint" x="740" y="470" width="120" height="100"/>
          <rect class="cube-faint" x="760" y="360" width="90" height="80"/>
        </g>

        <g class="cube cube-top-left">
          <rect class="cube-front" x="0" y="26" width="226" height="220"/>
          <rect class="cube-side" x="226" y="36" width="12" height="212"/>
        </g>
        <g class="cube cube-mid-left">
          <polygon class="cube-top" points="96,326 290,326 302,316 108,316"/>
          <rect class="cube-front" x="96" y="326" width="194" height="188"/>
          <polygon class="cube-side" points="290,326 302,316 302,500 290,514"/>
        </g>
        <g class="cube cube-top-right">
          <rect class="cube-side" x="678" y="168" width="10" height="156"/>
          <rect class="cube-front" x="688" y="160" width="178" height="164"/>
        </g>
        <g class="cube cube-small-right">
          <rect class="cube-top" x="630" y="372" width="86" height="8"/>
          <rect class="cube-front" x="630" y="380" width="86" height="112"/>
        </g>
        <g class="cube cube-edge-right">
          <rect class="cube-side" x="866" y="382" width="8" height="62"/>
          <rect class="cube-front" x="874" y="382" width="26" height="64"/>
        </g>
      </svg>

      <div class="card-content">
        <div class="brand-mark">
          <span class="brand-square"></span>
          <span class="brand-name">Dan Theroll</span>
        </div>
        <h1 class="person-name">Professor Dan Theroll</h1>
        <p class="tagline">Unlocking Early Numeracy</p>
        <ul class="contact-list">
          <li class="contact-email">info@dantheroll.net</li>
          <li class="contact-handle">#dantheroll26</li>
          <li class="contact-web">www.dantheroll.net</li>
          <li class="contact-phone">+44 7812 660 394</li>
        </ul>
      </div>
    </section>
  </main>
</body>
</html>
```